Cosmetic injections clinic needs a fresh looking business card

We need a business card using the supplied logo and color scheme to attract future clients to our clinic. It should be modern and fresh, eye catching and not too busy. Simple and to the point is best. I would like two sided designs with the front indicating address and contact information, and the back in full color with white logo and descriptive information also provided.
Target Market(s)
Clients looking for non surgical beauty enhancements.
Contact Information for Business Card
MeloraSkin
14, 618 Birchmont Way
Larchmere, Northvale
K2P 7W3
Phone: 587-412-6630
Email: info@meloraskin.com
Requirements
Must have
- -Logo supplied with the name and address of the clinic
- -Back of card in full color with white logo with A small line of text indicating both of the following: Anti aging consultants and cosmetic injectables
- Located inside the Voyager Wellness Group

```html
<!DOCTYPE html>
<html lang="en">
<head>
<meta charset="utf-8">
<title>MeloraSkin — Business Card</title>
<link rel="stylesheet" href="https://fonts.googleapis.com/css2?family=Alegreya+Sans:wght@400;500;700&display=swap">
<style>
  :root {
    --purple: #6b3f9c;
    --purple-deep: #5a2f8c;
    --pink: #e3449c;
    --pink-light: #ec5aa9;
    --white: #ffffff;
    --paper: #f6f6f7;
    --backdrop: #e4e4e6;
    --rule: rgba(255, 255, 255, 0.75);
    --card-w: 680px;
    --card-h: 390px;
    --radius: 28px;
  }
  * { box-sizing: border-box; margin: 0; padding: 0; }
  html, body {
    width: 1200px;
    height: 900px;
    overflow: hidden;
  }
  body {
    background: var(--backdrop);
    font-family: "Alegreya Sans", sans-serif;
    display: flex;
    flex-direction: column;
    align-items: center;
    justify-content: center;
    gap: 40px;
  }
  .card {
    width: var(--card-w);
    height: var(--card-h);
    border-radius: var(--radius);
    position: relative;
    overflow: hidden;
    box-shadow: 0 10px 24px rgba(0, 0, 0, 0.18);
  }

  /* Full-colour side */
  .card--colour {
    background: linear-gradient(100deg, var(--purple) 0%, var(--purple-deep) 30%, var(--pink) 62%, var(--pink-light) 100%);
    color: var(--white);
  }
  .colour-mark {
    position: absolute;
    left: 50px;
    top: 50%;
    transform: translateY(-50%);
    width: 310px;
    height: 310px;
    border-radius: 50%;
    background: rgba(255, 255, 255, 0.18);
  }
  .colour-name {
    position: absolute;
    left: 50px;
    width: 310px;
    top: 50%;
    transform: translateY(-50%);
    text-align: center;
    font-size: 42px;
    font-weight: 500;
    color: var(--white);
    letter-spacing: 0.5px;
  }
  .colour-info {
    position: absolute;
    right: 44px;
    top: 44px;
    width: 200px;
    text-transform: uppercase;
    letter-spacing: 1.5px;
  }
  .colour-info .tagline,
  .colour-info .location {
    font-size: 14px;
    line-height: 1.25;
    font-weight: 400;
  }
  .colour-info .rule {
    height: 1px;
    background: var(--rule);
    margin: 14px 0;
  }
  .colour-info .brand {
    font-size: 30px;
    font-weight: 500;
    letter-spacing: 1px;
    text-transform: none;
    line-height: 1.1;
  }

  /* Contact side */
  .card--contact {
    background: linear-gradient(120deg, var(--white) 0%, var(--paper) 55%, #e9e9eb 100%);
    color: var(--purple);
  }
  .contact-logo {
    position: absolute;
    left: 48px;
    top: 56px;
    display: flex;
    align-items: center;
    gap: 14px;
  }
  .contact-logo .dot {
    width: 58px;
    height: 58px;
    border-radius: 50%;
    background: var(--purple);
  }
  .contact-logo .name {
    font-size: 42px;
    font-weight: 500;
    color: var(--purple);
  }
  .contact-details {
    position: absolute;
    left: 60px;
    bottom: 48px;
    font-size: 19px;
    font-style: normal;
    line-height: 1.25;
    color: var(--purple);
  }
  .contact-details .clinic { font-weight: 700; }
  .contact-details .lines { margin-top: 2px; }
  .contact-details .reach { margin-top: 18px; }
  .contact-details .label { display: inline-block; width: 62px; }
</style>
</head>
<body>

  <section class="card card--colour" aria-label="Card back, full colour">
    <div class="colour-mark" aria-hidden="true"></div>
    <div class="colour-name">MeloraSkin</div>
    <div class="colour-info">
      <p class="tagline">Anti aging<br>consultants<br>and cosmetic<br>injectables</p>
      <div class="rule"></div>
      <p class="brand">MeloraSkin</p>
      <div class="rule"></div>
      <p class="location">Located inside<br>the Voyager<br>Wellness<br>Group</p>
    </div>
  </section>

  <section class="card card--contact" aria-label="Card front, contact details">
    <div class="contact-logo">
      <span class="dot" aria-hidden="true"></span>
      <span class="name">MeloraSkin</span>
    </div>
    <address class="contact-details">
      <div class="clinic">MeloraSkin</div>
      <div class="lines">14, 618 Birchmont Way<br>Larchmere, Northvale<br>K2P 7W3</div>
      <div class="reach">
        <span class="label">Phone:</span> 587 412 6630<br>
        <span class="label">Email:</span> info@meloraskin.com
      </div>
    </address>
  </section>

</body>
</html>
```